Stationary/business card for Custom Home builder
Pemberton Dwellings General Contractor
Simple
Travis Lindqvist
president
817 Calder Meadow Road
Dorrance Crossing, SC 29871
kbarlowbuilds@mailvero.net
Please use my logo

```html
<!DOCTYPE html>
<html lang="en">
<head>
<meta charset="utf-8">
<title>Pemberton Dwellings — Stationery Concepts</title>
<link rel="stylesheet" href="https://fonts.googleapis.com/css2?family=Open+Sans:wght@400;600;700&display=swap">
<style>
  :root {
    --backdrop: #ece4d6;
    --paper: #ffffff;
    --ink: #1f3350;
    --blue: #2a8fd6;
    --blue-deep: #1464a8;
    --blue-pale: #d8ecf9;
    --grey: #8a8f96;
    --night: #111418;
    --label: #5a5044;
  }
  * { box-sizing: border-box; margin: 0; padding: 0; }
  html, body { width: 1200px; height: 446px; overflow: hidden; }
  body {
    background: var(--backdrop);
    font-family: "Open Sans", Arial, sans-serif;
    color: var(--ink);
    position: relative;
  }
  .piece { position: absolute; background: var(--paper); box-shadow: 0 2px 6px rgba(0,0,0,.18); overflow: hidden; }
  .piece svg.wave { position: absolute; display: block; }
  .label {
    position: absolute; font-size: 7px; letter-spacing: 1.4px;
    text-transform: uppercase; color: var(--label); font-variant: small-caps;
  }
  .brand { font-weight: 700; color: var(--ink); line-height: 1.05; text-transform: uppercase; letter-spacing: .4px; }
  .brand span { display: block; }
  .small { font-size: 4.6px; line-height: 1.55; color: var(--grey); }
  .contact-row { display: flex; align-items: center; gap: 3px; }
  .dot { width: 4px; height: 4px; border-radius: 50%; background: var(--blue); flex: none; }

  /* business cards */
  .card-front { left: 12px; top: 210px; width: 120px; height: 56px; }
  .card-front .brand { position: absolute; left: 8px; top: 8px; font-size: 6px; }
  .card-front .details { position: absolute; right: 6px; top: 24px; text-align: right; font-size: 3.6px; }
  .card-back { left: 12px; top: 284px; width: 120px; height: 56px; background: var(--blue); }
  .card-back .brand { position: absolute; left: 0; right: 0; top: 20px; text-align: center; color: var(--paper); font-size: 6.5px; }

  /* letterheads */
  .letterhead-1 { left: 175px; top: 18px; width: 281px; height: 390px; }
  .letterhead-1 .brand { position: absolute; left: 22px; top: 22px; font-size: 9px; }
  .letterhead-1 .details { position: absolute; left: 168px; top: 20px; }
  .letterhead-2 { left: 477px; top: 18px; width: 281px; height: 390px; }
  .letterhead-2 .brand { position: absolute; left: 0; right: 0; top: 22px; text-align: center; font-size: 9px; }
  .letterhead-2 .footer { position: absolute; left: 60px; right: 20px; bottom: 20px; text-align: center; }

  /* envelopes */
  .envelope-back { left: 830px; width: 346px; height: 74px; }
  .envelope-back .brand { position: absolute; left: 0; right: 0; top: 22px; text-align: center; font-size: 6px; }
  .env-white { top: 22px; }
  .env-black { top: 104px; background: var(--night); }
  .env-black .brand { color: var(--paper); }
  .env-blue { top: 186px; }
  .env-blue .brand { color: var(--blue-deep); }
  .envelope-front { left: 794px; top: 284px; width: 262px; height: 134px; }
  .envelope-front .brand { position: absolute; left: 12px; top: 12px; font-size: 7px; }
  .envelope-front .return { position: absolute; left: 12px; top: 34px; }
  .envelope-front .addressee { position: absolute; left: 118px; top: 66px; font-size: 5.5px; line-height: 1.6; color: var(--ink); }
</style>
</head>
<body>

  <div class="label" style="left:12px; top:180px;">Stationery Concepts</div>

  <!-- business card front -->
  <div class="piece card-front">
    <div class="brand"><span>Pemberton Dwellings</span><span>General Contractor</span></div>
    <div class="details small">
      <div style="color:var(--ink);font-weight:700;">Travis Lindqvist</div>
      <div>President</div>
      <div>817 Calder Meadow Road</div>
      <div>Dorrance Crossing, SC 29871</div>
      <div>kbarlowbuilds@mailvero.net</div>
    </div>
    <svg class="wave" viewBox="0 0 120 56" width="120" height="56" style="left:0;top:0;">
      <path d="M0 40 C30 34 60 58 120 46 L120 56 L0 56 Z" fill="var(--blue)"/>
      <path d="M0 44 C34 38 66 60 120 50" fill="none" stroke="var(--blue-pale)" stroke-width="1"/>
    </svg>
  </div>
  <div class="label" style="left:12px; top:272px;">Business Card Front</div>

  <!-- business card back -->
  <div class="piece card-back">
    <svg class="wave" viewBox="0 0 120 56" width="120" height="56" style="left:0;top:0;">
      <path d="M0 42 C30 34 66 58 120 44 L120 56 L0 56 Z" fill="var(--blue-deep)"/>
    </svg>
    <div class="brand"><span>Pemberton Dwellings</span><span>General Contractor</span></div>
  </div>
  <div class="label" style="left:12px; top:346px;">Business Card Back</div>

  <!-- letterhead option 1 -->
  <div class="piece letterhead-1">
    <div class="brand"><span>Pemberton Dwellings</span><span>General Contractor</span></div>
    <div class="details small">
      <div class="contact-row"><i class="dot"></i>817 Calder Meadow Road</div>
      <div class="contact-row"><i class="dot"></i>Dorrance Crossing, SC 29871</div>
      <div class="contact-row"><i class="dot"></i>(843) 555-0172</div>
      <div class="contact-row"><i class="dot"></i>kbarlowbuilds@mailvero.net</div>
    </div>
    <svg class="wave" viewBox="0 0 281 70" width="281" height="70" style="left:0;bottom:0;">
      <path d="M0 30 C80 10 170 70 281 34 L281 70 L0 70 Z" fill="var(--blue)"/>
      <path d="M0 40 C90 22 180 78 281 44 L281 70 L0 70 Z" fill="var(--blue-deep)"/>
      <path d="M0 24 C80 4 170 64 281 28" fill="none" stroke="var(--blue)" stroke-width="1"/>
    </svg>
  </div>
  <div class="label" style="left:276px; top:426px;">Letter Head Option 1</div>

  <!-- letterhead option 2 -->
  <div class="piece letterhead-2">
    <svg class="wave" viewBox="0 0 60 390" width="60" height="390" style="left:0;top:0;">
      <path d="M0 0 L14 0 C44 120 10 250 40 390 L0 390 Z" fill="var(--blue)"/>
      <path d="M0 0 L6 0 C32 130 0 260 26 390 L0 390 Z" fill="var(--blue-deep)"/>
      <path d="M20 0 C50 120 16 250 46 390" fill="none" stroke="var(--blue)" stroke-width="1"/>
    </svg>
    <div class="brand"><span>Pemberton Dwellings</span><span>General Contractor</span></div>
    <div class="footer small">
      <div>817 Calder Meadow Road, Dorrance Crossing, SC 29871</div>
      <div>(843) 555-0172 &nbsp;|&nbsp; kbarlowbuilds@mailvero.net</div>
    </div>
  </div>
  <div class="label" style="left:578px; top:426px;">Letter Head Option 2</div>

  <!-- envelope backs -->
  <div class="piece envelope-back env-white">
    <svg class="wave" viewBox="0 0 346 74" width="346" height="74" style="left:0;top:0;">
      <path d="M0 0 L173 40 L346 0" fill="none" stroke="#c9ccd0" stroke-width="1"/>
    </svg>
    <div class="brand" style="top:46px;"><span>Pemberton Dwellings</span></div>
  </div>
  <div class="piece envelope-back env-black">
    <svg class="wave" viewBox="0 0 346 74" width="346" height="74" style="left:0;top:0;">
      <path d="M0 0 L173 42 L346 0 Z" fill="var(--paper)"/>
    </svg>
    <div class="brand" style="top:50px;"><span>Pemberton Dwellings</span></div>
  </div>
  <div class="piece envelope-back env-blue">
    <svg class="wave" viewBox="0 0 346 74" width="346" height="74" style="left:0;top:0;">
      <path d="M0 0 L173 40 L346 0" fill="none" stroke="#c9ccd0" stroke-width="1"/>
      <path d="M0 64 C110 54 230 74 346 62 L346 74 L0 74 Z" fill="var(--blue)"/>
    </svg>
    <div class="brand" style="top:44px;"><span>Pemberton Dwellings</span></div>
  </div>

  <!-- envelope front -->
  <div class="piece envelope-front">
    <div class="brand"><span>Pemberton Dwellings</span><span>General Contractor</span></div>
    <div class="return small">
      <div>817 Calder Meadow Road</div>
      <div>Dorrance Crossing, SC 29871</div>
    </div>
    <div class="addressee">
      <div>Mr. Dale Ostrander</div>
      <div>42 Harbor Pine Lane</div>
      <div>Lakewood Hollow, SC 29120</div>
    </div>
    <svg class="wave" viewBox="0 0 262 134" width="262" height="134" style="left:0;top:0;">
      <path d="M0 112 C60 100 120 134 180 134 L0 134 Z" fill="var(--blue)"/>
      <path d="M0 106 C64 94 126 130 190 134" fill="none" stroke="var(--blue)" stroke-width="1"/>
    </svg>
  </div>
  <div class="label" style="left:1032px; top:426px;">Envelope Option 3</div>

</body>
</html>
```